Customer Dashboard Design for Email Security SaaS

Mailbrook is a commercial email spam filter offered as a SaaS product, built and operated by a small German hosting provider. It protects business email accounts against spam, phishing, scam, and viruses using a multilayer filtering pipeline that combines traditional spam detection with AI-powered classification. The product runs entirely on German infrastructure, ensuring data sovereignty for European customers.

We need a complete redesign of the customer-facing dashboard. This is the web application where paying customers manage their email filtering: view their mail log, check quarantined emails, manage allow/blocklists, configure their settings, and handle their subscription. It is the primary touchpoint between Mailbrook and its customers.

Our customers are system administrators, IT managers at small-to-medium businesses, and operators of small hosting providers. They are technically competent but not designers. They expect professional, efficient tools that respect their time. They typically manage 10–500 email accounts and check the dashboard a few times per week, with heavier use during spam incidents.

We have attached the current mockups which really need to be replaced with something good looking.

Target Market(s)

System administrators, IT managers at small-to-medium businesses, and operators of small hosting providers.

Industry/Entity Type

SaaS

Number of Pages Required

5+ page

```html
<!DOCTYPE html>
<html lang="de">
<head>
<meta charset="utf-8">
<title>Mailbrook – Übersicht</title>
<link href="https://fonts.googleapis.com/css2?family=Figtree:wght@400;500;600&family=DM+Mono:wght@500&display=swap" rel="stylesheet">
<style>
  :root{
    --bg:#1a1918;
    --sidebar:#1c1b19;
    --card:#1f1e1c;
    --card-hi:#2b2823;
    --border:#302d29;
    --text:#ece8e2;
    --muted:#bdb5ab;
    --dim:#8c857c;
    --accent:#d9a152;
    --accent-bg:#33291d;
    --ham:#35b07c;
    --phish:#e07a35;
    --spam:#e04a4f;
    --news:#8cae48;
    --quar:#e2575c;
  }
  *{box-sizing:border-box;margin:0;padding:0}
  html,body{width:1200px;height:1111px;overflow:hidden}
  body{background:var(--bg);color:var(--text);font-family:"Figtree",sans-serif;position:relative}
  .mono{font-family:"DM Mono",monospace;font-weight:500}
  svg.icon{fill:none;stroke:currentColor;stroke-width:1.6;stroke-linecap:round;stroke-linejoin:round}

  .sidebar{position:absolute;left:0;top:0;width:218px;height:1111px;background:var(--sidebar);border-right:1px solid var(--border)}
  .brand{height:71px;border-bottom:1px solid var(--border);display:flex;align-items:center;padding-left:50px;font-size:24px;font-weight:500;letter-spacing:.2px}
  .nav{padding:20px 8px 0}
  .nav-item{height:37px;margin-bottom:9.7px;display:flex;align-items:center;gap:12px;padding-left:16px;font-size:15.5px;color:var(--text);border-radius:7px;position:relative}
  .nav-item svg{width:17px;height:17px;color:var(--muted)}
  .nav-item.active{background:var(--accent-bg);color:var(--accent)}
  .nav-item.active svg{color:var(--accent)}
  .count{position:absolute;right:4px;width:24px;height:20px;border-radius:10px;background:#3a2120;color:var(--quar);font-size:14px;display:flex;align-items:center;justify-content:center}
  .nav-sep{position:absolute;top:486px;left:0;right:0;border-top:1px solid var(--border)}
  .nav-group{position:absolute;top:516px;left:25px;font-size:9px;color:var(--dim);letter-spacing:.5px}
  .nav-admin{position:absolute;top:529px;left:8px;right:8px}
  .user{position:absolute;left:25px;bottom:18px;right:16px;display:flex;align-items:center;gap:8px}
  .avatar{width:28px;height:28px;border-radius:50%;background:#c78c4a;color:#3a2812;font-size:11px;font-weight:600;display:flex;align-items:center;justify-content:center}
  .user-name{font-size:13px;font-weight:600;line-height:1.1}
  .user-mail{font-size:11.5px;color:var(--muted)}
  .user svg{margin-left:auto;width:15px;height:15px;color:var(--muted)}

  .topbar{position:absolute;left:218px;right:0;top:0;height:71px;border-bottom:1px solid var(--border);display:flex;align-items:center;padding-left:24px;gap:12px;font-size:15px;color:var(--muted)}
  .topbar > svg{width:21px;height:21px}
  .theme{position:absolute;right:24px;top:11px;width:92px;height:49px;border:1px solid var(--border);border-radius:9px;display:flex;align-items:center;justify-content:space-around;padding:0 6px}
  .theme span{width:38px;height:34px;border-radius:7px;display:flex;align-items:center;justify-content:center}
  .theme span.on{background:#2e2c28}
  .theme svg{width:20px;height:20px;color:var(--text)}

  .main{position:absolute;left:243px;top:71px;width:932px}
  .greet{margin-top:28px;font-size:23px;font-weight:500}
  .mode{margin-top:8px;display:inline-flex;align-items:center;gap:8px;height:26px;padding:0 22px 0 10px;border:1px solid #6e5330;border-radius:13px;background:#2a241c;color:var(--accent);font-size:12px}
  .mode i{width:5px;height:5px;border-radius:50%;background:var(--accent)}

  .card{background:var(--card);border:1px solid var(--border);border-radius:7px}
  .row1{margin-top:32px;display:grid;grid-template-columns:454px 226px 226px;gap:13px;height:131px}
  .row1 .card{padding:18px 21px}
  .row1 .card.hi{background:var(--card-hi);border-color:#3a362f}
  .label{display:flex;align-items:center;gap:7px;font-size:13px;color:var(--muted);text-transform:uppercase}
  .label svg{width:19px;height:19px}
  .hi .label svg{color:var(--accent)}
  .big{font-size:44px;margin-top:4px;line-height:1.05}
  .mid{font-size:30px;margin-top:8px;line-height:1.1}
  .sub{font-size:13px;color:var(--text);margin-top:6px}
  .hi .sub{margin-top:8px}

  .row2{margin-top:11px;display:grid;grid-template-columns:repeat(5,1fr);gap:13px;height:131px}
  .row2 .card{padding:16px 17px}
  .row2 .label{text-transform:none;color:var(--text);font-size:13.3px}
  .row2 .label svg{color:var(--muted)}
  .row2 .num{font-size:31px;margin-top:12px;line-height:1}
  .row2 .sub{margin-top:12px}

  .chart{margin-top:13px;height:496px;position:relative}
  .chart-title{position:absolute;left:30px;top:32px;font-size:22px;font-weight:500}
  .range{position:absolute;left:733px;top:22px;width:176px;height:49px;border:1px solid var(--border);border-radius:8px;display:flex;align-items:center;padding:0 7px;gap:4px;font-size:15.5px}
  .range span{height:35px;display:flex;align-items:center;justify-content:center;border-radius:6px;padding:0 12px}
  .range span.on{background:#2c2a26;width:80px}
  .chart svg.plot{position:absolute;left:0;top:0}
  .tip{position:absolute;left:440px;top:181px;width:89px;height:101px;background:#1c1b1a;border:1px solid var(--border);border-radius:6px;padding:14px 15px;font-size:10px;line-height:17.5px}
  .tip .d{color:var(--text);margin-bottom:5px}

  .links{margin-top:14px;display:grid;grid-template-columns:460px 460px;gap:12px;height:86px}
  .link{position:relative;padding:14px 0 0 77px}
  .link.hi{background:var(--card-hi);border-color:#3a362f}
  .link > svg.lead{position:absolute;left:26px;top:18px;width:36px;height:36px;color:var(--muted)}
  .link.hi > svg.lead{color:var(--accent)}
  .link h3{font-size:19px;font-weight:500;letter-spacing:.4px}
  .link p{font-size:13px;margin-top:8px}
  .go{position:absolute;right:12px;top:25px;width:34px;height:35px;border:1px solid #8a6737;border-radius:6px;display:flex;align-items:center;justify-content:center;color:var(--accent)}
  .go svg,.chev svg{width:14px;height:14px}
  .chev{position:absolute;right:26px;top:36px;color:var(--text)}
</style>
</head>
<body>

<aside class="sidebar">
  <div class="brand">Mailbrook</div>
  <nav class="nav">
    <div class="nav-item active"><svg class="icon" viewBox="0 0 24 24"><path d="M3 10l9-7 9 7v10a1 1 0 0 1-1 1H4a1 1 0 0 1-1-1z"/></svg>Übersicht</div>
    <div class="nav-item"><svg class="icon" viewBox="0 0 24 24"><path d="M4 6h16M4 12h16M4 18h16"/></svg>Mail-Log</div>
    <div class="nav-item"><svg class="icon" viewBox="0 0 24 24"><path d="M12 3l10 18H2z"/><path d="M12 10v5M12 18v.01"/></svg>Quarantäne<span class="count">4</span></div>
    <div class="nav-item"><svg class="icon" viewBox="0 0 24 24"><rect x="3" y="5" width="18" height="14" rx="2"/><path d="M3 12h5l2 3h4l2-3h5"/></svg>Postfächer</div>
    <div class="nav-item"><svg class="icon" viewBox="0 0 24 24"><path d="M4 6h14M4 11h10M4 16h7M14 17l3 3 5-6"/></svg>Allowlist</div>
    <div class="nav-item"><svg class="icon" viewBox="0 0 24 24"><circle cx="12" cy="12" r="9"/><path d="M6 18L18 6"/></svg>Blocklist</div>
    <div class="nav-item"><svg class="icon" viewBox="0 0 24 24"><circle cx="12" cy="12" r="3"/><path d="M12 2l2 3 3.5-.5 1 3.5 3 2-1.5 3 1.5 3-3 2-1 3.5L14 19l-2 3-2-3-3.5.5-1-3.5-3-2L4 11 2.5 8l3-2 1-3.5L10 5z"/></svg>Einstellungen</div>
    <div class="nav-item"><svg class="icon" viewBox="0 0 24 24"><rect x="5" y="3" width="14" height="18" rx="1"/><path d="M9 8h6M9 12h6M9 16h4"/></svg>Abrechnung</div>
  </nav>
  <div class="nav-sep"></div>
  <div class="nav-group">VERWALTUNG</div>
  <div class="nav-admin"><div class="nav-item"><svg class="icon" viewBox="0 0 24 24"><circle cx="10" cy="7" r="4"/><path d="M3 21c0-4 3-7 7-7"/><circle cx="17" cy="17" r="3"/></svg>Administration</div></div>
  <div class="user">
    <div class="avatar">LB</div>
    <div><div class="user-name">Lukas Berger</div><div class="user-mail">l.berger@beispiel.de</div></div>
    <svg class="icon" viewBox="0 0 24 24"><path d="M14 4H5v16h9M10 12h11M17 8l4 4-4 4"/></svg>
  </div>
</aside>

<header class="topbar">
  <svg class="icon" viewBox="0 0 24 24"><rect x="3" y="4" width="18" height="16" rx="2"/><path d="M9 4v16"/></svg>
  Übersicht
  <div class="theme">
    <span class="on"><svg class="icon" viewBox="0 0 24 24"><path d="M20 14A8 8 0 1 1 10 4a6.5 6.5 0 0 0 10 10z"/></svg></span>
    <span><svg class="icon" viewBox="0 0 24 24"><circle cx="12" cy="12" r="4"/><path d="M12 2v2M12 20v2M2 12h2M20 12h2M5 5l1.5 1.5M17.5 17.5L19 19M5 19l1.5-1.5M17.5 6.5L19 5"/></svg></span>
  </div>
</header>

<main class="main">
  <h1 class="greet">Guten Morgen, Jonas</h1>
  <div class="mode"><i></i>Beobachtungsmodus — E-Mails werden analysiert, nicht blockiert</div>

  <section class="row1">
    <div class="card hi">
      <div class="label"><svg class="icon" viewBox="0 0 24 24"><rect x="3" y="5" width="18" height="14" rx="2"/><path d="M3 7l9 6 9-6"/></svg>Letzte 24 Stunden</div>
      <div class="big mono">1.247</div>
      <div class="sub">849 zugestellt · 398 abgefangen</div>
    </div>
    <div class="card">
      <div class="label"><svg class="icon" viewBox="0 0 24 24"><rect x="3" y="5" width="18" height="16" rx="2"/><path d="M3 10h18M8 3v4M16 3v4M9 15l2 2 4-4"/></svg>7 Tage</div>
      <div class="mid mono">8.492</div>
      <div class="sub">68% zugestellt</div>
    </div>
    <div class="card">
      <div class="label"><svg class="icon" viewBox="0 0 24 24"><rect x="3" y="5" width="18" height="16" rx="2"/><path d="M3 10h18M8 3v4M16 3v4M9 15l2 2 4-4"/></svg>30 Tage</div>
      <div class="mid mono">34.610</div>
      <div class="sub">71% zugestellt</div>
    </div>
  </section>

  <section class="row2">
    <div class="card">
      <div class="label"><svg class="icon" viewBox="0 0 24 24"><path d="M8 2h8l6 6v8l-6 6H8l-6-6V8z"/><path d="M12 7v6M12 16v.01"/></svg>Spam blockiert</div>
      <div class="num mono" style="color:var(--accent)">4,218</div>
      <div class="sub">+12 % ggü. Vormonat</div>
    </div>
    <div class="card">
      <div class="label"><svg class="icon" viewBox="0 0 24 24"><circle cx="12" cy="4" r="2"/><path d="M12 6v10a4 4 0 0 1-8 0v-2l2 2"/></svg>Phishing erkannt</div>
      <div class="num mono" style="color:var(--phish)">143</div>
      <div class="sub">+3 heute</div>
    </div>
    <div class="card">
      <div class="label"><svg class="icon" viewBox="0 0 24 24"><rect x="7" y="7" width="10" height="13" rx="5"/><path d="M9 4l2 3M15 4l-2 3M3 11h4M17 11h4M3 17h4M17 17h4M12 10v10"/></svg>Viren abgefangen</div>
      <div class="num mono" style="color:var(--ham)">12</div>
      <div class="sub">0 heute</div>
    </div>
    <div class="card">
      <div class="label"><svg class="icon" viewBox="0 0 24 24"><rect x="3" y="3" width="18" height="18" rx="1"/><path d="M7 8h10M7 12h10M7 16h6"/></svg>Newsletter sortiert</div>
      <div class="num mono" style="color:var(--news)">891</div>
      <div class="sub">34 heute</div>
    </div>
    <div class="card">
      <div class="label"><svg class="icon" viewBox="0 0 24 24"><path d="M12 3l10 18H2z"/><path d="M12 10v5M12 18v.01"/></svg>In Quarantäne</div>
      <div class="num mono" style="color:var(--quar)">23</div>
      <div class="sub">Überprüfung erforderlich</div>
    </div>
  </section>

  <section class="card chart">
    <h2 class="chart-title">E-Mail-Volumen</h2>
    <div class="range"><span class="on">7 Tage</span><span>30 Tage</span></div>
    <svg class="plot" width="932" height="496" viewBox="0 0 932 496" font-family="Figtree, sans-serif" font-size="15.5" fill="#bdb5ab">
      <defs>
        <linearGradient id="gHam" x1="0" y1="0" x2="0" y2="1"><stop offset="0" stop-color="#35b07c" stop-opacity=".22"/><stop offset="1" stop-color="#35b07c" stop-opacity=".06"/></linearGradient>
        <linearGradient id="gSpam" x1="0" y1="0" x2="0" y2="1"><stop offset="0" stop-color="#e04a4f" stop-opacity=".22"/><stop offset="1" stop-color="#e04a4f" stop-opacity=".05"/></linearGradient>
      </defs>
      <g stroke="#3a3732" stroke-dasharray="4 4">
        <path d="M82 109H887M82 188H887M82 267H887M82 345H887"/>
        <path d="M198 109V424M314 109V424M430 109V424M546 109V424M661 109V424M777 109V424M887 109V424"/>
      </g>
      <path d="M82 165C140 165 140 135 198 135C256 135 256 211 314 211C372 211 372 128 430 128C488 128 488 142 546 142C604 142 604 109 661 109C719 109 719 192 777 192C832 192 832 153 887 153V424H82Z" fill="url(#gHam)"/>
      <path d="M82 165C140 165 140 135 198 135C256 135 256 211 314 211C372 211 372 128 430 128C488 128 488 142 546 142C604 142 604 109 661 109C719 109 719 192 777 192C832 192 832 153 887 153" fill="none" stroke="#35b07c" stroke-width="2.2"/>
      <path d="M82 382C140 382 140 367 198 367C256 367 256 389 314 389C372 389 372 358 430 358C488 358 488 373 546 373C604 373 604 350 661 350C719 350 719 384 777 384C832 384 832 378 887 378V424H82Z" fill="url(#gSpam)"/>
      <path d="M82 382C140 382 140 367 198 367C256 367 256 389 314 389C372 389 372 358 430 358C488 358 488 373 546 373C604 373 604 350 661 350C719 350 719 384 777 384C832 384 832 378 887 378" fill="none" stroke="#e04a4f" stroke-width="2"/>
      <path d="M82 417C140 417 140 414 198 414C256 414 256 419 314 419C372 419 372 410 430 410C488 410 488 415 546 415C604 415 604 408 661 408C719 408 719 419 777 419C832 419 832 416 887 416" fill="none" stroke="#e07a35" stroke-width="2"/>
      <path d="M82 109V424H887" fill="none" stroke="#6d6861" stroke-width="1.2"/>
      <g stroke="#6d6861"><path d="M76 109H82M76 188H82M76 267H82M76 345H82M76 424H82M82 424V430M198 424V430M314 424V430M430 424V430M546 424V430M661 424V430M777 424V430M887 424V430"/></g>
      <line x1="430" y1="109" x2="430" y2="424" stroke="#ece8e2" stroke-width="1.2"/>
      <circle cx="430" cy="128" r="5" fill="#35b07c" stroke="#ece8e2" stroke-width="1.2"/>
      <circle cx="430" cy="358" r="5" fill="#e04a4f" stroke="#ece8e2" stroke-width="1.2"/>
      <circle cx="430" cy="410" r="5" fill="#e07a35" stroke="#ece8e2" stroke-width="1.2"/>
      <g text-anchor="end"><text x="60" y="114">340</text><text x="60" y="193">255</text><text x="60" y="272">170</text><text x="60" y="350">85</text><text x="60" y="429">0</text></g>
      <g text-anchor="middle"><text x="89" y="451">10 Mar</text><text x="202" y="451">11 Mar</text><text x="317" y="451">12 Mar</text><text x="437" y="451">13 Mar</text><text x="547" y="451">14 Mar</text><text x="663" y="451">15 Mar</text><text x="780" y="451">16 Mar</text><text x="886" y="451">17 Mar</text></g>
    </svg>
    <div class="tip">
      <div class="d">13. Mär</div>
      <div style="color:var(--ham)">ham : 320</div>
      <div style="color:var(--phish)">phishing : 15</div>
      <div style="color:var(--spam)">spam : 71</div>
    </div>
  </section>

  <section class="links">
    <div class="card link hi">
      <svg class="icon lead" viewBox="0 0 24 24"><path d="M12 3l10 18H2z"/><path d="M12 10v5M12 18v.01"/></svg>
      <h3>Quarantäne prüfen</h3>
      <p>23 E-Mails warten auf Überprüfung</p>
      <span class="go"><svg class="icon" viewBox="0 0 24 24"><path d="M9 5l7 7-7 7"/></svg></span>
    </div>
    <div class="card link">
      <svg class="icon lead" viewBox="0 0 24 24"><rect x="3" y="5" width="18" height="14" rx="2"/><path d="M3 7l9 6 9-6"/></svg>
      <h3>E-Mail-Protokoll</h3>
      <p>Alle verarbeiteten E-Mails durchsuchen</p>
      <span class="chev"><svg class="icon" viewBox="0 0 24 24"><path d="M9 5l7 7-7 7"/></svg></span>
    </div>
  </section>
</main>

</body>
</html>
```